digger and truck hire

this is a new business - Digger and Truck
we would like to include the attached photo of the digger and truck - as the truck is red and the digger is green
maybe either black or white lettering which ever suits

Industry/Entity Type

Business

Contact Information for Business Card

RDL - Ruddas 2.5t Mini Digger and 7t Tip Truck -Hire, full attachments, augers, trenching, site preparation, small aggregate deliveries
Phone 0218365914
rudda.rdl@plinto.co.nz

```html
<!DOCTYPE html>
<html lang="en">
<head>
<meta charset="utf-8">
<title>RDL Business Card</title>
<link rel="stylesheet" href="https://fonts.googleapis.com/css2?family=Michroma&family=Oswald:wght@500;600&display=swap">
<style>
  :root {
    --backdrop: #c9c9c9;
    --card-white: #ffffff;
    --brand-red: #c8141c;
    --band-red: #d0161e;
    --ink: #111111;
    --plate-dark: #141414;
    --plate-mid: #262626;
    --steel-line: #9a9a9a;
    --text-light: #ffffff;
  }
  * { margin: 0; padding: 0; box-sizing: border-box; }
  html, body {
    width: 1200px; height: 900px; overflow: hidden;
    background: var(--backdrop);
  }
  .business-card {
    position: absolute; left: 100px; top: 150px;
    width: 1000px; height: 600px;
    border-radius: 38px; overflow: hidden;
    background: var(--card-white);
  }
  .brand-header {
    position: absolute; left: 0; top: 0; width: 100%; height: 240px;
    background: var(--card-white);
  }
  .brand-name {
    position: absolute; left: 0; right: 0; top: 44px;
    text-align: center;
    font-family: "Michroma", sans-serif;
    font-size: 84px; line-height: 1;
    color: var(--brand-red);
  }
  .business-title {
    position: absolute; left: 0; right: 0; top: 162px;
    text-align: center;
    font-family: "Michroma", sans-serif;
    font-size: 23px; font-weight: 400;
    color: var(--ink);
    text-transform: uppercase;
    letter-spacing: -0.3px;
  }
  .steel-rule {
    position: absolute; left: 0; top: 240px; width: 100%; height: 6px;
    background: var(--steel-line);
  }
  .services-band {
    position: absolute; left: 0; top: 246px; width: 100%; height: 32px;
    background: var(--band-red);
    display: flex; align-items: center; justify-content: center;
    font-family: "Oswald", sans-serif; font-weight: 600;
    font-size: 19px; letter-spacing: 0.6px;
    color: var(--text-light); text-transform: uppercase;
  }
  .plate-section {
    position: absolute; left: 0; top: 278px; width: 100%; height: 322px;
    background: radial-gradient(ellipse at 55% 40%, var(--plate-mid), var(--plate-dark) 75%);
    border-top: 3px solid var(--steel-line);
  }
  .fleet-photo {
    position: absolute; right: 0; top: 0; width: 440px; height: 100%;
    background: linear-gradient(100deg, rgba(20,20,20,0) 0%, #3a3a3a 25%, #4a4640 55%, #a3262a 82%, #b8343a 100%);
  }
  .contact-list {
    position: absolute; left: 60px; top: 130px;
    list-style: none;
    font-family: "Oswald", sans-serif; font-weight: 500;
    color: var(--text-light); text-transform: uppercase;
  }
  .contact-item {
    display: flex; align-items: center; gap: 18px;
    font-size: 44px; line-height: 1; height: 56px; margin-bottom: 12px;
  }
  .contact-icon { width: 40px; height: 40px; flex: none; }
</style>
</head>
<body>
  <div class="business-card">
    <header class="brand-header">
      <div class="brand-name">RDL</div>
      <h1 class="business-title">Ruddas 2.5t Mini Digger and 7t Tip Truck</h1>
    </header>
    <div class="steel-rule"></div>
    <div class="services-band">Hire, full attachments, augers, trenching, site preparation, small aggregate deliveries</div>
    <section class="plate-section">
      <div class="fleet-photo" role="img" aria-label="Photo of the green mini digger strapped on the deck of the red tip truck"></div>
      <ul class="contact-list">
        <li class="contact-item">
          <svg class="contact-icon" viewBox="0 0 24 24" aria-hidden="true">
            <path fill="#d0161e" d="M6.6 10.8a15.1 15.1 0 0 0 6.6 6.6l2.2-2.2a1 1 0 0 1 1-.25 11.4 11.4 0 0 0 3.6.57 1 1 0 0 1 1 1V20a1 1 0 0 1-1 1A17 17 0 0 1 3 4a1 1 0 0 1 1-1h3.5a1 1 0 0 1 1 1c0 1.25.2 2.45.57 3.6a1 1 0 0 1-.25 1z"/>
          </svg>
          <span>021 836 5914</span>
        </li>
        <li class="contact-item">
          <svg class="contact-icon" viewBox="0 0 24 24" aria-hidden="true">
            <rect x="2" y="5" width="20" height="14" rx="1.5" fill="#d0161e"/>
            <path d="M2.5 6l9.5 7 9.5-7" fill="none" stroke="#141414" stroke-width="1.6"/>
          </svg>
          <span>rudda.rdl@plinto.co.nz</span>
        </li>
      </ul>
    </section>
  </div>
</body>
</html>
```